Financial Advisor Brochure to attract new clients

I am launching a new career as a Financial Advisor and a flier that shows what services I offer and why I decided to go back to work at this point in my life. I have a deep desire to help people meet their dreams and believe that a solid financial foundation provides the ability to live your life as you want to and not how you have to. I created a simple flier but know that so much more can be done to catch a persons eye.

Target Market(s)

Entrepeneurs and Woman in all stages of life.

Industry/Entity Type

Financial Advisor

Font styles to use
Sans Serif

Colors
00AB8E
00BBA5
67D7C9
C6EFE9
E9F9F6

Requirements
Must have
• my photo, contact information and Tessaly Logo

```html
<!DOCTYPE html>
<html lang="en">
<head>
<meta charset="utf-8">
<title>Renata Holloway – Financial Advisor Flyer</title>
<link href="https://fonts.googleapis.com/css2?family=Barlow+Condensed:wght@500;600;700&family=Montserrat:wght@400;500;600&display=swap" rel="stylesheet">
<style>
  :root {
    --teal: #2bb593;
    --teal-deep: #00ab8e;
    --mint: #c6efe9;
    --gray-top: #8a9292;
    --gray-bottom: #c3c6c5;
    --ink: #3d4042;
    --white: #ffffff;
    --backdrop: #dcdcdc;
  }
  * { box-sizing: border-box; margin: 0; padding: 0; }
  html, body {
    width: 1200px; height: 2344px; overflow: hidden;
    background: var(--backdrop);
  }
  .flyer {
    position: absolute; left: 58px; top: 405px;
    width: 1083px; height: 1533px;
    background: var(--teal);
    box-shadow: 0 6px 18px rgba(0,0,0,.25);
    font-family: "Montserrat", sans-serif;
    color: var(--white);
  }
  .hero {
    position: absolute; left: 0; top: 0; width: 1083px; height: 722px;
    background: linear-gradient(180deg, var(--gray-top) 0%, #a9adac 55%, var(--gray-bottom) 100%);
    overflow: hidden;
  }
  .hero__portrait {
    position: absolute; right: 0; top: 0; width: 560px; height: 722px;
    background:
      radial-gradient(ellipse 38% 30% at 62% 22%, rgba(140,96,70,.75) 0%, rgba(140,96,70,0) 100%),
      radial-gradient(ellipse 55% 48% at 60% 72%, #1f9c86 0%, #2d9583 45%, rgba(160,165,164,0) 100%);
  }
  .hero__text { position: absolute; left: 52px; top: 62px; width: 640px; }
  .name {
    font-family: "Barlow Condensed", sans-serif; font-weight: 700;
    font-size: 76px; line-height: 80px; color: var(--mint); letter-spacing: .5px;
    white-space: nowrap;
  }
  .title {
    font-family: "Barlow Condensed", sans-serif; font-weight: 600;
    font-size: 48px; line-height: 52px; margin-top: 4px;
  }
  .label {
    font-family: "Barlow Condensed", sans-serif; font-weight: 600;
    font-size: 26px; line-height: 30px; color: var(--mint);
  }
  .label--profile { margin-top: 28px; }
  .profile {
    font-weight: 600; font-size: 18px; line-height: 22px;
    width: 440px; margin-top: 8px;
  }
  .cta {
    display: inline-block; margin-top: 30px; margin-left: -7px;
    background: var(--white); color: var(--teal-deep);
    font-family: "Barlow Condensed", sans-serif; font-weight: 600;
    font-size: 27px; line-height: 38px; padding: 0 17px; border-radius: 8px;
  }
  .phone {
    display: flex; align-items: center; gap: 14px; margin-top: 8px;
    font-family: "Barlow Condensed", sans-serif; font-weight: 700;
    font-size: 42px; line-height: 48px;
  }
  .label--email { margin-top: 24px; }
  .label--web { margin-top: 20px; }
  .contact { font-size: 18px; line-height: 26px; margin-top: 8px; }

  .story {
    position: absolute; left: 53px; top: 756px; width: 403px;
    font-size: 18.3px; line-height: 21.8px; text-align: justify;
  }
  .story p + p { margin-top: 22px; }

  .services {
    position: absolute; left: 496px; top: 722px; width: 587px; height: 791px;
    background: var(--white); color: var(--ink); padding: 28px 30px 0 36px;
  }
  .services__heading {
    font-family: "Barlow Condensed", sans-serif; font-weight: 600;
    font-size: 37px; line-height: 40px; color: var(--ink);
  }
  .service__tag {
    display: inline-block; margin-top: 20px;
    background: var(--teal); color: var(--white);
    font-family: "Barlow Condensed", sans-serif; font-weight: 600;
    font-size: 28px; line-height: 33px; padding: 0 14px; border-radius: 7px;
  }
  .service__tag:first-of-type { margin-top: 14px; }
  .service__list { list-style: none; margin-top: 7px; }
  .service__list li {
    position: relative; padding-left: 18px;
    font-size: 18.3px; line-height: 22px; margin-top: 5px;
  }
  .service__list li::before {
    content: ""; position: absolute; left: 1px; top: 8px;
    width: 8px; height: 8px; border-radius: 50%; background: var(--teal);
  }
</style>
</head>
<body>
  <article class="flyer">
    <section class="hero">
      <div class="hero__portrait" role="img" aria-label="Portrait photo of the advisor, smiling, in a teal blouse, arms resting on a table"></div>
      <div class="hero__text">
        <h1 class="name">RENATA HOLLOWAY</h1>
        <h2 class="title">Financial Advisor</h2>
        <h3 class="label label--profile">PROFILE</h3>
        <p class="profile">Passionate about helping empower you with knowledge to make informed financial decisions throughout all of life’s stages and help you achieve your goals.</p>
        <div class="cta">CALL FOR AN APPOINTMENT</div>
        <div class="phone">
          <svg width="34" height="34" viewBox="0 0 24 24" aria-hidden="true">
            <path fill="#fff" d="M6.6 10.8a15.2 15.2 0 0 0 6.6 6.6l2.2-2.2a1 1 0 0 1 1-.25 11.4 11.4 0 0 0 3.6.57 1 1 0 0 1 1 1V20a1 1 0 0 1-1 1A17 17 0 0 1 3 4a1 1 0 0 1 1-1h3.5a1 1 0 0 1 1 1c0 1.25.2 2.45.57 3.57a1 1 0 0 1-.25 1z"/>
            <path fill="none" stroke="#fff" stroke-width="1.8" stroke-linecap="round" d="M14.5 3.5a6.5 6.5 0 0 1 6 6M14.2 7a3 3 0 0 1 2.8 2.8"/>
          </svg>
          407-555-0186
        </div>
        <h3 class="label label--email">EMAIL:</h3>
        <p class="contact">renata.holloway@tessalyadvisors.com</p>
        <h3 class="label label--web">WEBSITE:</h3>
        <p class="contact">www.tessalyadvisors.com</p>
      </div>
    </section>

    <section class="story">
      <p>As a business owner, wife, and mother of two teenagers, I understand the struggles you face juggling your personal, business, and financial life.</p>
      <p>I grew up in a home where my parents had opposing money habits. My Dad was a big spender and mom was a saver. Through the years, I saw how my mom’s consistent savings grew while Dad’s style led to many financial ups and downs. This made a huge impression on me and sparked my continued interest in all things finance.</p>
      <p>Having an entrepreneurial personality and ability to explain concepts in a relatable manner has provided me with many opportunities. In 2018, After decades of running a sales agency, I sold my company to spend time with my kids and family but my interest in Finance never waned. Now that our kids are thriving teenagers, I started a new career as a licensed Financial Advisor with a heart to help you achieve your financial dreams.</p>
      <p>The financial world is changing rapidly, and it can be confusing on how to maneuver through these times. My goal is to pull out the emotions that cloud judgement and help you make better decisions with your long-range goals in mind</p>
    </section>

    <section class="services">
      <h2 class="services__heading">Financial planning services offered:</h2>
      <div class="service__tag">Transition Planning</div>
      <ul class="service__list">
        <li>Divorce planning.</li>
        <li>Strategy and guidance pre, during, and postdivorce</li>
      </ul>
      <div class="service__tag">Retirement planning</div>
      <ul class="service__list">
        <li>Current portfolio analysis</li>
        <li>Timeline asset and income planning</li>
        <li>Tax and estate review and projections</li>
      </ul>
      <div class="service__tag">Real estate acquisition or sale</div>
      <ul class="service__list">
        <li>Acquisition or dissolution of real estate.<br>Individual or portfolio</li>
      </ul>
      <div class="service__tag">Business sale or purchase:</div>
      <ul class="service__list">
        <li>Company valuations</li>
        <li>Tax impact analysis</li>
        <li>Strategy implementation for funds<br>received from sale.</li>
      </ul>
      <div class="service__tag">Estate planning</div>
      <ul class="service__list">
        <li>Strategies for creating future generational wealth.</li>
      </ul>
      <div class="service__tag">New Investors:</div>
      <ul class="service__list">
        <li>Assistance in opening investment and<br>retirement acc</li>
      </ul>
    </section>
  </article>
</body>
</html>
```